FRONT BUS CARD:

We were maybe thinking to have the text in a "common seal" which is an oval shape. Or CROWN VAULT underlined, then AUSTRALIA underneath...

Picture to have in the seal, or next to the words if seal not used: Gold Bars (3 of them), or scales of justice..

LOGO and pic and font to be in shiny gold.
We want 1 black background design and 1 white background design.

CROWN VAULT TRADERS

```html
<!DOCTYPE html>
<html lang="en">
<head>
<meta charset="utf-8">
<title>Crown Vault Traders – Business Cards</title>
<link rel="stylesheet" href="https://fonts.googleapis.com/css2?family=PT+Serif:wght@400;700&display=swap">
<style>
  :root {
    --backdrop: #ebebeb;
    --card-black: #000000;
    --card-white: #ffffff;
    --gold: #d9a93a;
    --gold-soft: #e8c46a;
    --text-light: #ffffff;
    --text-dark: #111111;
  }
  * { margin: 0; padding: 0; box-sizing: border-box; }
  html, body {
    width: 1200px;
    height: 534px;
    overflow: hidden;
    background: var(--backdrop);
    font-family: "PT Serif", Georgia, serif;
  }
  .stage { position: relative; width: 1200px; height: 534px; }

  .card {
    position: absolute;
    top: 119px;
    width: 525px;
    height: 300px;
    border-radius: 22px;
    overflow: hidden;
  }
  .card--front { left: 62px; background: var(--card-black); }
  .card--back { left: 621px; background: var(--card-white); }

  .brand {
    position: absolute;
    left: 0;
    width: 100%;
    display: flex;
    align-items: center;
    justify-content: center;
    gap: 14px;
  }
  .card--front .brand { top: 78px; }
  .card--back .brand { top: 70px; }
  .brand__dot {
    width: 16px;
    height: 16px;
    border-radius: 50%;
    background: var(--gold);
    flex: none;
  }
  .brand__name {
    color: var(--gold);
    font-weight: 700;
    font-size: 34px;
    line-height: 1.1;
    letter-spacing: 1px;
    text-align: center;
  }

  .web-band {
    position: absolute;
    left: 0;
    top: 238px;
    width: 100%;
    height: 38px;
    background: var(--card-white);
    display: flex;
    align-items: center;
    justify-content: center;
  }
  .web-band__url {
    color: var(--text-dark);
    font-weight: 700;
    font-size: 15px;
    letter-spacing: 0.3px;
  }

  .contact-band {
    position: absolute;
    left: 0;
    top: 213px;
    width: 100%;
    height: 87px;
    background: var(--card-black);
  }
  .person {
    position: absolute;
    left: 79px;
    top: 24px;
  }
  .person__name {
    color: var(--gold-soft);
    font-size: 19px;
    line-height: 1.2;
  }
  .person__role {
    color: var(--text-light);
    font-size: 13px;
    margin-top: 3px;
  }
  .contact-list {
    position: absolute;
    left: 252px;
    top: 14px;
    list-style: none;
  }
  .contact-list li {
    color: var(--text-light);
    font-size: 12.5px;
    line-height: 20.5px;
  }
  .contact-list__label { color: var(--gold-soft); margin-right: 4px; }
</style>
</head>
<body>
<main class="stage">

  <section class="card card--front" aria-label="Business card front">
    <div class="brand">
      <span class="brand__dot"></span>
      <span class="brand__name">CROWN VAULT<br>TRADERS</span>
    </div>
    <div class="web-band">
      <span class="web-band__url">www.CrownVaultTraders.com</span>
    </div>
  </section>

  <section class="card card--back" aria-label="Business card back">
    <div class="brand">
      <span class="brand__dot"></span>
      <span class="brand__name">CROWN VAULT<br>TRADERS</span>
    </div>
    <div class="contact-band">
      <div class="person">
        <p class="person__name">Marcus Ellery</p>
        <p class="person__role">Owner/Founder</p>
      </div>
      <ul class="contact-list">
        <li><span class="contact-list__label">p :</span>123-418-7702</li>
        <li><span class="contact-list__label">e :</span>marcus@crownvaulttraders.com</li>
        <li><span class="contact-list__label">w :</span>www.crownvaulttraders.com</li>
      </ul>
    </div>
  </section>

</main>
</body>
</html>
```